Business Cards for a company that provides webstore services to veterinarians

We need business cards designed for our main service PawCartHub. PawCartHub is a webstore that veterinarian clinics can use to that will allow their clients to purchase products for their pets. Our company is Brindlow Veterinary Solutions (BVS). Our mission statement is We love pets! We will do everything possible to facilitate along, healthy and happy relationship with their families.

Target Market(s)

Veterinarians

Industry/Entity Type

Veterinary

Contact Information for Business Card

I would like the design to incorporate the colours our our company. Cards should have room for employee name, title (only necessary in two instances), phone number, mobile number, email address and linkedin symbol and related profile name ie Marla Quinton. I would like the PawCartHub logo to appear on one side and BVS logo to appear on the other. I will need both an english and french version. I can provide the french translation. Please focus on english version and then we will translate

Colors

Designer to choose colors to be used in the design.

Requirements
Must have
• one side - PawCartHub logo with persons name, phone number, mobile number, email address
• second side - BVS logo
• colours should be consistent with our company. colours are as follows:
• Red
• RGB: 190 / 30 / 45
• CYMK: 14 / 100 / 90 /10
• Hex: #BE1E2D
• Gray
• RGB: 88 / 89 / 86
• CYMK: 3 / 2 / 0 /64
• Hex: #585956
Nice to have
• address of company - can be on either side address is 4817 Feldmoor Street Suite 305 Burlington ON K2R 6T4. Toll free number will vary depending on person
• Linkedin symbol and name of person
• on second side with BVS logo our company's mission statement
Should not have
• nothing comes to mind

```html
<!DOCTYPE html>
<html lang="en">
<head>
<meta charset="utf-8">
<title>PawCartHub and Brindlow Veterinary Solutions Business Cards</title>
<link href="https://fonts.googleapis.com/css2?family=Lato:wght@400;700;900&display=swap" rel="stylesheet">
<style>
  :root {
    --brand-red: #BE1E2D;
    --brand-gray: #585956;
    --swoosh-gray: #5e5f5c;
    --paper: #ffffff;
    --stage: #2b2b2b;
    --ink-light: #ffffff;
  }
  * { box-sizing: border-box; margin: 0; padding: 0; }
  html, body {
    width: 1200px; height: 880px; overflow: hidden;
    background: var(--stage);
    font-family: "Lato", Arial, sans-serif;
  }
  .canvas { position: relative; width: 1200px; height: 880px; }

  .card {
    position: absolute;
    width: 560px; height: 320px;
    border-radius: 22px;
    overflow: hidden;
    box-shadow: 0 10px 30px rgba(0,0,0,0.45);
  }

  /* Back side: company name and mission */
  .card-back { left: 60px; top: 70px; background: var(--brand-red); color: var(--ink-light); }
  .card-back .figure-shade {
    position: absolute; right: 40px; top: 20px;
    width: 170px; height: 240px; border-radius: 80px 80px 20px 20px;
    background: linear-gradient(180deg, rgba(160,20,34,0.55), rgba(190,30,45,0));
  }
  .company-name {
    position: absolute; left: 30px; right: 30px; top: 110px;
    display: flex; align-items: center; justify-content: center; gap: 12px;
  }
  .company-name .name-dot {
    width: 18px; height: 18px; border-radius: 50%; background: var(--ink-light); flex: none;
  }
  .company-name .name-text {
    font-weight: 700; font-size: 30px; line-height: 1.1; letter-spacing: 0.2px;
  }
  .mission {
    position: absolute; left: 50px; right: 50px; top: 212px;
    text-align: center; font-size: 15px; line-height: 1.45; font-weight: 400;
  }

  /* Front side: service name and contact details */
  .card-front { left: 580px; top: 490px; background: var(--paper); color: var(--brand-gray); }
  .card-front .swoosh { position: absolute; right: 0; top: 0; width: 200px; height: 320px; }
  .service-name {
    position: absolute; left: 40px; top: 40px;
    font-size: 50px; font-weight: 700; color: var(--brand-gray); letter-spacing: -0.5px;
  }
  .contact { position: absolute; left: 40px; top: 138px; font-size: 14px; line-height: 1.35; }
  .person { display: flex; align-items: center; gap: 10px; margin-bottom: 12px; }
  .person .profile-dot {
    width: 22px; height: 22px; border-radius: 50%; border: 2px solid var(--brand-red); flex: none;
  }
  .person-name { font-size: 19px; font-weight: 900; letter-spacing: 0.3px; line-height: 1.1; }
  .person-name .surname { color: var(--brand-red); }
  .person-title { font-size: 14px; font-weight: 400; }
  .address { margin: 0 0 10px 32px; }
  .lines { list-style: none; }
  .lines li { display: flex; align-items: center; gap: 10px; }
  .lines .icon { width: 22px; height: 22px; flex: none; }
</style>
</head>
<body>
<main class="canvas">

  <section class="card card-back" aria-label="Card back">
    <div class="figure-shade" role="img" aria-label="Faint silhouette of a person with a pet"></div>
    <div class="company-name">
      <span class="name-dot"></span>
      <span class="name-text">Brindlow Veterinary Solutions</span>
    </div>
    <p class="mission">We love pets! We will do everything possible to facilitate along<br>healthy and happy relationship with their families.</p>
  </section>

  <section class="card card-front" aria-label="Card front">
    <svg class="swoosh" viewBox="0 0 200 320" aria-hidden="true">
      <path d="M60 0 C150 60 70 200 200 290 L200 0 Z" fill="var(--swoosh-gray)"/>
      <path d="M80 0 C170 60 95 200 200 275 L200 0 Z" fill="var(--paper)"/>
      <path d="M100 0 C185 60 120 200 200 262 L200 0 Z" fill="var(--brand-red)"/>
    </svg>

    <div class="service-name">PawCartHub</div>

    <div class="contact">
      <div class="person">
        <span class="profile-dot"></span>
        <div>
          <div class="person-name">MARLA <span class="surname">QUINTON</span></div>
          <div class="person-title">Manager</div>
        </div>
      </div>
      <p class="address">4817 Feldmoor Street Suite<br>305 Burlington ON K2R 6T4</p>
      <ul class="lines">
        <li>
          <svg class="icon" viewBox="0 0 22 22" aria-hidden="true"><circle cx="11" cy="11" r="10" fill="var(--brand-red)"/><path d="M7 6h3l1 3-2 1c1 2 2 3 4 4l1-2 3 1v3c-6 0-10-4-10-10z" fill="#fff"/></svg>
          (905) 555-0142
        </li>
        <li>
          <svg class="icon" viewBox="0 0 22 22" aria-hidden="true"><circle cx="11" cy="11" r="10" fill="var(--brand-red)"/><rect x="7.5" y="5" width="7" height="12" rx="1.5" fill="#fff"/><rect x="8.8" y="6.5" width="4.4" height="7.5" fill="var(--brand-red)"/></svg>
          (905) 555-0178
        </li>
        <li>
          <svg class="icon" viewBox="0 0 22 22" aria-hidden="true"><circle cx="11" cy="11" r="10" fill="var(--brand-red)"/><rect x="5.5" y="7" width="11" height="8" fill="#fff"/><path d="M5.5 7l5.5 4.5 5.5-4.5" fill="none" stroke="var(--brand-red)" stroke-width="1.2"/></svg>
          hello@pawcarthub.ca
        </li>
      </ul>
    </div>
  </section>

</main>
</body>
</html>
```